Letter head incorporating Our values and our Clover & Kite logo

here are our current letterheads, similar look and feel but incorporating our values logo too.
I have attached some of our flyers to give an idea of our look and feel of our brand

```html
<!DOCTYPE html>
<html lang="en">
<head>
<meta charset="utf-8">
<title>Clover &amp; Kite Letterhead</title>
<link rel="stylesheet" href="https://fonts.googleapis.com/css2?family=Open+Sans:wght@400;600&family=Poppins:wght@300;400;500&display=swap">
<style>
  :root {
    --brand-blue: #29a8e0;
    --sun-yellow: #f5e91c;
    --grass-dark: #8cc63f;
    --grass-light: #a3d05a;
    --ink: #333333;
    --body-grey: #666666;
    --paper: #ffffff;
  }
  * { margin: 0; padding: 0; box-sizing: border-box; }
  html, body { width: 922px; height: 1200px; overflow: hidden; background: var(--paper); }
  .letterhead { position: relative; width: 922px; height: 1200px; background: var(--paper); font-family: "Open Sans", sans-serif; color: var(--ink); }

  .brand-band {
    position: absolute; left: 0; top: 48px; width: 368px; height: 122px;
    background: var(--brand-blue); border-radius: 0 61px 61px 0;
    display: flex; align-items: center; padding-left: 98px;
  }
  .brand-name { font-family: "Open Sans", sans-serif; font-weight: 600; font-size: 30px; color: #ffffff; letter-spacing: 0.5px; }

  .school-contact { position: absolute; right: 73px; top: 62px; font-family: "Poppins", sans-serif; font-weight: 300; font-size: 13.5px; color: var(--ink); text-align: right; }
  .contact-row { display: flex; justify-content: flex-end; align-items: flex-start; gap: 7px; line-height: 17px; }
  .contact-row + .contact-row { margin-top: 8px; }
  .contact-icon { width: 18px; height: 18px; flex: none; margin-top: 0; }

  .sender { position: absolute; left: 81px; top: 263px; }
  .sender-name { font-family: "Open Sans", sans-serif; font-weight: 600; font-size: 24px; color: var(--brand-blue); line-height: 30px; }
  .sender-title { font-size: 13px; color: var(--ink); margin-top: 2px; }
  .sender-details { list-style: none; margin-top: 19px; font-size: 16px; color: var(--ink); }
  .sender-details li { line-height: 24px; display: flex; }
  .detail-label { color: var(--brand-blue); font-weight: 600; width: 32px; }

  .letter-date { position: absolute; right: 84px; top: 406px; font-size: 19.5px; color: var(--ink); }

  .letter-body { position: absolute; left: 83px; top: 471px; width: 755px; font-size: 15.4px; line-height: 22.4px; color: var(--body-grey); text-align: justify; }
  .letter-body p + p { margin-top: 22px; }

  .signature { position: absolute; left: 98px; top: 838px; width: 134px; height: 76px; }
  .signatory { position: absolute; left: 83px; top: 924px; font-family: "Poppins", sans-serif; font-weight: 500; font-size: 21px; color: var(--ink); }

  .footer-scene { position: absolute; left: 0; top: 900px; width: 922px; height: 300px; }
  .footer-web { position: absolute; left: 0; width: 922px; top: 1146px; text-align: center; font-family: "Poppins", sans-serif; font-size: 14px; letter-spacing: 6px; color: #ffffff; }
</style>
</head>
<body>
<main class="letterhead">
  <header>
    <div class="brand-band"><span class="brand-name">Clover &amp; Kite</span></div>

    <address class="school-contact">
      <div class="contact-row"><span>27 Wattlebird Lane<br>MARLOW NSW 2190</span>
        <svg class="contact-icon" viewBox="0 0 18 18"><rect width="18" height="18" rx="3" fill="var(--brand-blue)"/><path d="M9 3.5a4 4 0 0 0-4 4c0 3 4 7 4 7s4-4 4-7a4 4 0 0 0-4-4z" fill="#fff"/><circle cx="9" cy="7.5" r="1.5" fill="var(--brand-blue)"/></svg></div>
      <div class="contact-row"><span>(02) 5550 1234</span>
        <svg class="contact-icon" viewBox="0 0 18 18"><rect width="18" height="18" rx="3" fill="var(--brand-blue)"/><path d="M5.5 4h2l1 3-1.3 1a7 7 0 0 0 2.8 2.8l1-1.3 3 1v2c0 .6-.5 1-1 1A9 9 0 0 1 4.5 5c0-.5.4-1 1-1z" fill="#fff"/></svg></div>
      <div class="contact-row"><span>0400 555 218</span>
        <svg class="contact-icon" viewBox="0 0 18 18"><rect width="18" height="18" rx="3" fill="var(--brand-blue)"/><rect x="5.5" y="3.5" width="7" height="11" rx="1" fill="none" stroke="#fff" stroke-width="1.5"/></svg></div>
      <div class="contact-row"><span>hello@cloverandkite.edu.au</span>
        <svg class="contact-icon" viewBox="0 0 18 18"><rect width="18" height="18" rx="3" fill="var(--brand-blue)"/><rect x="3.5" y="5" width="11" height="8" fill="none" stroke="#fff" stroke-width="1.3"/><path d="M3.5 5l5.5 4.5L14.5 5" fill="none" stroke="#fff" stroke-width="1.3"/></svg></div>
    </address>
  </header>

  <section class="sender">
    <h1 class="sender-name">Mara Ellison</h1>
    <p class="sender-title">Chief Director</p>
    <ul class="sender-details">
      <li><span class="detail-label">A :</span>512 Harbour Street, Sydney NSW 2000</li>
      <li><span class="detail-label">W :</span>www.cloverandkite.edu.au</li>
      <li><span class="detail-label">P :</span>+61 2 5550 9876</li>
      <li><span class="detail-label">M :</span>office@cloverandkite.edu.au</li>
    </ul>
  </section>

  <p class="letter-date">12 December, 2025</p>

  <article class="letter-body">
    <p>Lorem ipsum dolor sit amet, consectetuer adipiscing elit, sed diam nonummy nibh euismod tincidunt ut laoreet dolore magna aliquam erat volutpat. Ut wisi enim ad minim veniam, quis nostrud exerci tation ullamcorper suscipit lobortis nisl ut aliquip ex ea commodo consequat. Duis autem vel eum iriure dolor in hendrerit in vulputate velit esse molestie consequat, vel illum dolore eu feugiat nulla facilisis at vero eros et accumsan et iusto odio dignissim qui blandit praesent luptatum zzril delenit augue duis dolore te feugait nulla facilisi.</p>
    <p>Lorem ipsum dolor sit amet, cons ectetuer adipiscing elit, sed diam nonummy nibh euismod tincidunt ut laoreet dolore magna aliquam erat volutpat. Ut wisi enim ad minim veniam, quis nostrud exerci tation ullamcorper suscipit lobortis nisl ut aliquip ex ea commodo consequat.</p>
    <p>Lorem ipsum dolor sit amet, consectetuer adipiscing elit, sed diam nonummy nibh euismod tincidunt ut laoreet dolore magna aliquam eratveniam, quis nostrud exerci tation ullamcorper suscipit lobortis nisl ut aliquip ex ea commodo consequat. Lorem ipsum dolor sit zamet, consectetuer adipiscing elit, sed diam nonummy nibh euismod tincidunt.</p>
  </article>

  <svg class="signature" role="img" aria-label="Handwritten signature" viewBox="0 0 134 76"><rect width="134" height="76" rx="4" fill="#f1f1f1"/></svg>
  <p class="signatory">Mr. Tom Ellison</p>

  <footer>
    <svg class="footer-scene" viewBox="0 0 922 300" aria-hidden="false">
      <defs>
        <radialGradient id="sun-glow" cx="0.7" cy="0.7" r="0.7">
          <stop offset="0" stop-color="var(--sun-yellow)"/>
          <stop offset="1" stop-color="#fbf6a8"/>
        </radialGradient>
        <linearGradient id="tree-books" x1="0" x2="1">
          <stop offset="0" stop-color="#5fb446"/>
          <stop offset="1" stop-color="#e0634a"/>
        </linearGradient>
      </defs>
      <g role="img" aria-label="Illustration of a bright sun with a child flying a kite">
        <rect x="610" y="20" width="312" height="230" rx="20" fill="url(#sun-glow)"/>
      </g>
      <g role="img" aria-label="Illustration of trees beside a stack of books">
        <rect x="85" y="161" width="160" height="92" rx="12" fill="url(#tree-books)"/>
      </g>
      <path class="hill-back" d="M0 268 Q470 165 922 240 L922 300 L0 300 Z" fill="var(--grass-dark)"/>
      <path class="hill-front" d="M0 282 Q470 180 922 252 L922 300 L0 300 Z" fill="var(--grass-light)"/>
    </svg>
    <p class="footer-web">CLOVERANDKITE.EDU.AU</p>
  </footer>
</main>
</body>
</html>
```